Brivelo Website Design - Wordpress

Need a website WordPress design for our existing website that we just stood up. The logo is already in place and name. Brivelo.example We are a company which makes connections with our clients through educating them and providing networking events. We would like for the website to show a VIP/special feel to it.

Target Market(s)

Business executives and employees. Age group 26-65 in the following sectors:
- Technology
- Human Resources
- Finance
- Sales

Industry/Entity Type

Technical Service

Number of Pages Required

4 page

Font styles to use
Sans Serif

Requirements
Must have
• Must be something for Wordpress
Nice to have
• Would like this to be professional but look cutting edge and VIP.

```html
<!DOCTYPE html>
<html lang="en">
<head>
<meta charset="utf-8">
<title>Brivelo — Expand Your Business</title>
<link href="https://fonts.googleapis.com/css2?family=Questrial&display=swap" rel="stylesheet">
<style>
:root{
  --green:#3a8f3d;
  --green-light:#4caf50;
  --ink:#111;
  --dark:#161616;
  --panel:#262626;
  --text:#222;
  --muted:#666;
  --white:#fff;
  --line:#555;
}
*{box-sizing:border-box;margin:0;padding:0}
html,body{width:1200px;height:2941px;overflow:hidden}
body{position:relative;font-family:"Questrial",sans-serif;color:var(--text);background:var(--white)}
.abs{position:absolute}

/* hero */
.hero{left:0;top:0;width:1200px;height:1082px;background:radial-gradient(circle at 30% 10%,#262626 0%,#141414 60%,#0d0d0d 100%)}
.brand{left:78px;top:28px;display:flex;align-items:center;gap:14px;color:var(--white);font-size:30px;letter-spacing:4px}
.brand-mark{width:44px;height:44px;background:var(--green)}
.main-nav{right:56px;top:36px;display:flex;gap:32px;font-size:14px;color:var(--white);letter-spacing:.5px}
.main-nav .active{color:var(--green-light)}
.hero-title{left:78px;top:238px;font-size:50px;color:var(--green-light);font-weight:400}
.hero-sub{left:78px;top:314px;font-size:29px;color:var(--white)}
.hero-copy{left:78px;top:378px;width:600px;font-size:19px;line-height:29px;color:var(--white)}

/* pillars card */
.pillars{left:78px;top:625px;width:1122px;height:355px;background:var(--white)}
.pillars-tail{left:800px;top:980px;width:400px;height:102px;background:var(--white)}
.scroll-btn{left:571px;top:596px;width:58px;height:58px;border-radius:50%;background:var(--green);box-shadow:0 0 0 6px rgba(255,255,255,.35);display:flex;align-items:center;justify-content:center}
.pillar{top:690px;width:200px}
.pillar svg{display:block;margin-bottom:14px}
.pillar h3{font-size:22px;font-weight:400;letter-spacing:1px;color:#333}
.pillar p{font-size:17px;color:var(--muted);margin-top:10px}
.quote{left:176px;top:876px;width:624px;height:206px;background:var(--panel);color:#eee;font-size:13.5px;line-height:27px;text-align:center;padding:54px 22px 0}

/* offers */
.section-title{font-size:38px;font-weight:400;color:var(--ink)}
.offers-title{left:0;top:1145px;width:1200px;text-align:center}
.offer{top:1215px;width:240px;text-align:center}
.offer svg{display:block;margin:0 auto}
.offer h3{font-size:17px;font-weight:400;letter-spacing:1px;color:#333;margin-top:20px}
.offer p{font-size:13.5px;line-height:26px;color:var(--muted);margin-top:10px}

/* welcome */
.welcome-title{left:78px;top:1602px;font-size:38px}
.welcome-copy{left:78px;top:1664px;width:500px;font-size:13.5px;line-height:25px;color:var(--muted)}
.explore{left:108px;top:1800px;width:221px;height:52px;border:2px solid #222;display:flex;align-items:center;gap:18px;padding-left:18px;font-size:17px;letter-spacing:1px;color:var(--green)}
.explore::before{content:"";width:34px;height:2px;background:#222}
.deco-line{height:2px;background:#222}
.strategy-title{left:623px;top:1603px;font-size:20px;color:#222}
.strategy-copy{left:623px;top:1642px;width:500px;font-size:13.5px;line-height:25px;color:var(--muted)}
.strategy-copy p+p{margin-top:12px}
.frame-bottom{left:78px;top:1912px;width:1045px;height:1px;background:#777}
.frame-left{left:78px;top:1820px;width:1px;height:93px;background:#777}

/* newsletter */
.news-band{left:78px;top:2044px;width:1016px;height:259px;background:var(--green)}
.news-card{left:102px;top:2068px;width:1021px;height:261px;background:var(--white);box-shadow:0 6px 24px rgba(0,0,0,.12);text-align:center;padding-top:68px;font-size:17px;line-height:32px;color:#555}
.news-form{left:351px;top:2218px;width:496px;height:42px;border:1px solid #ccc;border-radius:21px;display:flex;align-items:center;justify-content:space-between;padding-left:22px;font-size:12px;color:#999}
.news-form span.btn{width:158px;height:42px;margin-right:-1px;border-radius:21px;background:var(--green);color:var(--white);font-size:15px;display:flex;align-items:center;justify-content:center}

/* footer */
.footer{left:0;top:2438px;width:1200px;height:503px;background:var(--dark)}
.contact-bar{left:78px;top:2424px;width:1045px;height:144px;background:var(--panel);display:flex;align-items:center;padding-left:54px}
.contact{display:flex;align-items:flex-start;gap:18px;color:var(--white)}
.contact .ico{width:50px;height:50px;border:1px solid #888;border-radius:50%;display:flex;align-items:center;justify-content:center;margin-top:4px}
.contact h4{font-size:19px;font-weight:400;margin-bottom:8px}
.contact p{font-size:13px;line-height:25px;color:#ddd}
.foot-nav{left:78px;top:2603px;display:flex;gap:18px;font-size:13px;color:#888}
.foot-nav i{font-style:normal;color:#555}
.social{top:2592px;width:42px;height:42px;border-radius:50%;border:2px solid var(--white)}
.social.fill{background:var(--white)}
.foot-rule{left:0;top:2656px;width:1200px;height:1px;background:#333}
.foot-brand{left:78px;top:2740px;display:flex;align-items:center;gap:18px;color:var(--white);font-size:36px;letter-spacing:6px}
.foot-brand .brand-mark{width:64px;height:64px}
.foot-offers{left:884px;top:2714px;color:var(--white)}
.foot-offers h4{font-size:19px;font-weight:400;margin-bottom:14px}
.foot-offers ul{list-style:none;display:grid;grid-template-columns:133px 120px;row-gap:18px;font-size:13px}
.foot-offers li{display:flex;align-items:center;gap:10px}
.foot-offers li::before{content:"";width:10px;height:10px;background:var(--green)}
.copyright{left:0;top:2877px;width:1200px;height:64px;background:#000;border-top:1px solid #444;color:#ccc;font-size:13px;display:flex;align-items:center;justify-content:center}
</style>
</head>
<body>

<section class="abs hero" aria-label="Hero"></section>
<div class="abs brand"><span class="brand-mark"></span>BRIVELO</div>
<nav class="abs main-nav"><span class="active">EVENTS</span><span>EXPAND</span><span>X</span><span>ABOUT</span><span>CONNECT</span></nav>
<h1 class="abs hero-title">Expand Your Business</h1>
<p class="abs hero-sub">It's about our unique X Strategy</p>
<p class="abs hero-copy">BRIVELO provides impactful connection opportunities to help educate, equip and expand you and your business</p>

<div class="abs pillars"></div>
<div class="abs pillars-tail"></div>
<div class="abs scroll-btn"><svg width="20" height="12" viewBox="0 0 20 12"><path d="M2 2l8 8 8-8" fill="none" stroke="#fff" stroke-width="2"/></svg></div>

<div class="abs pillar" style="left:170px">
  <svg width="42" height="42" viewBox="0 0 42 42"><path d="M21 6c-8 0-14 5-14 12 0 4 2 6 2 9s3 9 12 9 12-6 12-9 2-5 2-9c0-7-6-12-14-12zM21 6v30" fill="none" stroke="#3d7fbf" stroke-width="2"/></svg>
  <h3>MIND</h3><p>Thought</p>
</div>
<div class="abs pillar" style="left:405px">
  <svg width="46" height="42" viewBox="0 0 46 42"><circle cx="23" cy="21" r="18" fill="none" stroke="#8e44ad" stroke-width="2"/><path d="M23 12c5 5 5 12 0 17-5-5-5-12 0-17zM11 20c6 0 10 4 12 9-6 0-10-4-12-9zM35 20c-6 0-10 4-12 9 6 0 10-4 12-9z" fill="none" stroke="#8e44ad" stroke-width="2"/></svg>
  <h3>SOUL</h3><p>Intuition</p>
</div>
<div class="abs pillar" style="left:645px">
  <svg width="44" height="42" viewBox="0 0 44 42"><path d="M22 38S4 26 4 14a9 9 0 0 1 18-3 9 9 0 0 1 18 3c0 12-18 24-18 24z" fill="none" stroke="#d9322b" stroke-width="2"/></svg>
  <h3>HEART</h3><p>Emotion</p>
</div>
<div class="abs pillar" style="left:890px">
  <svg width="44" height="42" viewBox="0 0 44 42"><circle cx="22" cy="21" r="18" fill="none" stroke="#e6a817" stroke-width="2"/><path d="M25 8l-9 15h7l-3 11 9-15h-7z" fill="none" stroke="#e6a817" stroke-width="2"/></svg>
  <h3>STREANTH</h3><p>Energy</p>
</div>

<blockquote class="abs quote">Lorem Ipsum is simply dummy text of the printing and typesetting industry. Lorem Ipsum has been the industry's standard dummy text ever since the 1500s, when an unknown printer took a galley of type and scrambled it to make a type specimen book it has survived not only five centuries.</blockquote>

<h2 class="abs section-title offers-title">What We Offer You</h2>

<div class="abs offer" style="left:78px">
  <svg width="96" height="106" viewBox="0 0 96 106"><path d="M48 3l43 25v50L48 103 5 78V28z" fill="none" stroke="#3a8f3d" stroke-width="1.5"/><rect x="23" y="28" width="50" height="50" fill="#3a8f3d"/><path d="M48 40l-18 8 18 8 18-8zM38 52v8c6 4 14 4 20 0v-8M64 49v10" fill="none" stroke="#fff" stroke-width="2"/></svg>
  <h3>EDUCATE</h3><p>At BRIVELO, we provide effective training and learning as the foundation for building a healthy, successful company.</p>
</div>
<div class="abs offer" style="left:344px">
  <svg width="96" height="106" viewBox="0 0 96 106"><path d="M48 3l43 25v50L48 103 5 78V28z" fill="none" stroke="#3a8f3d" stroke-width="1.5"/><rect x="23" y="28" width="50" height="50" fill="#3a8f3d"/><path d="M33 62l15-20 15 20M40 62h16" fill="none" stroke="#fff" stroke-width="3"/></svg>
  <h3>EQUIP</h3><p>Through our connected ecosystem of companies, we'll help find the right partners for equipping you to move forward.</p>
</div>
<div class="abs offer" style="left:613px">
  <svg width="96" height="106" viewBox="0 0 96 106"><path d="M48 3l43 25v50L48 103 5 78V28z" fill="none" stroke="#3a8f3d" stroke-width="1.5"/><rect x="23" y="28" width="50" height="50" fill="#3a8f3d"/><path d="M34 46h26l-6-6M62 60H36l6 6" fill="none" stroke="#fff" stroke-width="3"/></svg>
  <h3>EXCHANGE</h3><p>We connect you with others who have successfully implemented our X Strategy to facilitate growth in their business.</p>
</div>
<div class="abs offer" style="left:881px">
  <svg width="96" height="106" viewBox="0 0 96 106"><path d="M48 3l43 25v50L48 103 5 78V28z" fill="none" stroke="#3a8f3d" stroke-width="1.5"/><rect x="23" y="28" width="50" height="50" fill="#3a8f3d"/><path d="M32 38l32 30M64 38L32 68M32 38h8M32 38v8M64 38h-8M64 38v8M32 68h8M32 68v-8M64 68h-8M64 68v-8" fill="none" stroke="#fff" stroke-width="3"/></svg>
  <h3>EXPAND</h3><p>Our goal is to help you and your business increase productivity and scale through effective strategy and healthy culture.</p>
</div>

<h2 class="abs section-title welcome-title">Welcome to Brivelo</h2>
<p class="abs welcome-copy">We use a green diamond in our logo to represent your company's culture. Green speaks of health. And growth. And life. That's what we want to help you do with your business – make it healthy and productive</p>
<div class="abs deco-line" style="left:108px;top:1784px;width:96px"></div>
<div class="abs explore">EXPLORE MORE</div>
<div class="abs deco-line" style="left:255px;top:1866px;width:96px"></div>
<h3 class="abs strategy-title">Our unique X Strategy</h3>
<div class="abs strategy-copy">
  <p>BRIVELO is powerfully effective because our approach is humanolistic. Our materials are founded upon the idea that Culture is a Person. Marcus developed his philosophy on culture over more than three decades, learning from leaders and communities around the globe.</p>
  <p>We understand at the deepest level that culture is the heartbeat of your company, and as a healthy, strong heart means a healthy, strong person, culture works in a similar fashion. We use the letter X to illustrate this.</p>
</div>
<div class="abs frame-left"></div>
<div class="abs frame-bottom"></div>

<div class="abs news-band"></div>
<div class="abs news-card">signup to our newsletter to get latest update<br>and news from us</div>
<div class="abs news-form">Enter your email<span class="btn">SUBSCRIBE</span></div>

<footer class="abs footer"></footer>
<div class="abs contact-bar">
  <div class="contact" style="width:375px">
    <span class="ico"><svg width="18" height="22" viewBox="0 0 18 22"><path d="M9 21s7-8 7-13A7 7 0 0 0 2 8c0 5 7 13 7 13z" fill="none" stroke="#fff" stroke-width="1.6"/><circle cx="9" cy="8" r="2.5" fill="#fff"/></svg></span>
    <div><h4>Address</h4><p>Lorem Ipsum is simply dummy<br>text of the printing.</p></div>
  </div>
  <div class="contact" style="width:326px">
    <span class="ico"><svg width="20" height="20" viewBox="0 0 20 20"><path d="M4 2l4 1 1 4-2 2c1 2 3 4 5 5l2-2 4 1 1 4-2 2C9 19 1 11 2 4z" fill="#fff"/></svg></span>
    <div><h4>Phone</h4><p>1-855-555-0142</p></div>
  </div>
  <div class="contact">
    <span class="ico"><svg width="20" height="16" viewBox="0 0 20 16"><rect x="1" y="2" width="18" height="12" rx="1" fill="#fff"/><path d="M1 3l9 6 9-6" fill="none" stroke="#262626" stroke-width="1.6"/></svg></span>
    <div><h4>Email</h4><p>connect@brivelo.example</p></div>
  </div>
</div>
<nav class="abs foot-nav"><span>Events</span><i>|</i><span>Expands</span><i>|</i><span>X</span><i>|</i><span>About</span><i>|</i><span>Connect</span></nav>
<span class="abs social fill" style="left:982px"></span>
<span class="abs social" style="left:1031px"></span>
<span class="abs social" style="left:1080px"></span>
<div class="abs foot-rule"></div>
<div class="abs foot-brand"><span class="brand-mark"></span>BRIVELO</div>
<div class="abs foot-offers">
  <h4>What We Offer You</h4>
  <ul><li>Education</li><li>Exchange</li><li>Equip</li><li>Expand</li></ul>
</div>
<div class="abs copyright">©BRIVELO. 2019 – All Rights Reserved.</div>

</body>
</html>
```